We are looking for a logo AND business card design.  We are a sponsor who provides an international experience for individuals both in the U.S. and abroad to improve work skills, gain life experiences, and language skills while making the world a better, more understood place to live. 

Business card:  Lorna Pickett

Bright Horizon Passage, 5427 Amber Hollow Lane, Ashford Bay, NC 28999  (770) 481-3027   www.brighthorizonpassage.example

Logo does not have to be literal.  A good graphic with words would be acceptable also.

Logo Text

Requirements
Must have
• Please embed fonts in the vector file so we and our printers can add / change names as we grow AND AI file.
Nice to have
• Open to font and color but must be professional.  Name does not need to be in logo.
Should not have
• Pastels or flourescents.

```html
<!DOCTYPE html>
<html lang="en">
<head>
<meta charset="utf-8">
<title>Bright Horizon Passage – Business Card Concepts</title>
<link rel="stylesheet" href="https://fonts.googleapis.com/css2?family=Arimo:ital,wght@0,400;0,700;1,700&family=Allura&display=swap">
<style>
  :root{
    --blue:#0a68b4;
    --blue-light:#b9d6ee;
    --ink:#1e1e1e;
    --logo-ink:#2f2f2f;
    --paper:#ffffff;
    --page:#ffffff;
    --sans:"Arimo", Arial, Helvetica, sans-serif;
    --script:"Allura", cursive;
  }
  *{box-sizing:border-box;margin:0;padding:0}
  html,body{width:800px;height:1200px;overflow:hidden;background:var(--page)}
  body{position:relative;font-family:var(--sans);color:var(--ink)}

  .card{position:absolute;width:349px;height:224px;background:var(--paper);overflow:hidden;
        box-shadow:2px 3px 4px rgba(0,0,0,.35);border:1px solid #d8d8d8}
  .card--blue{background:var(--blue);border-color:var(--blue);color:#fff}
  .col-a{left:43px}.col-b{left:419px}
  .row-1{top:73px}.row-2{top:340px}.row-3{top:613px}.row-4{top:880px}

  /* wordmark: one colour, one weight, one plain circle */
  .brand{position:absolute;white-space:nowrap;font-size:20px;line-height:22px;color:var(--logo-ink);font-weight:400;padding-right:2px}
  .brand__line{display:block}
  .brand__mark{position:absolute;right:0;top:-8px;width:30px;height:30px;border:2px solid var(--blue);border-radius:50%}
  .brand--white{color:#fff}
  .brand--white .brand__mark{border-color:#fff}

  .text{position:absolute;font-size:11.5px;line-height:16px;white-space:nowrap}
  .right{text-align:right}
  .center{text-align:center;left:0;right:0}
  .strong-blue{color:var(--blue);font-weight:700}
  .name-bold{font-weight:700;font-size:12.5px}
  .email b{font-weight:700}
  .lbl{color:var(--blue);font-weight:700;margin-right:3px}
  .lbl-gap{margin-left:8px}

  .script{position:absolute;font-family:var(--script);font-size:27px;line-height:30px;white-space:nowrap}
  .rule{position:absolute;height:1.5px;background:var(--blue)}
  .rule--white{background:#fff}

  .band{position:absolute;left:0;right:0;background:var(--blue)}
  .glow{position:absolute;left:70px;top:-70px;width:240px;height:240px;border-radius:50%;
        background:radial-gradient(circle,rgba(255,255,255,.35),rgba(255,255,255,0) 70%)}
  .url{position:absolute;left:18px;bottom:26px;color:#fff;font-size:14.5px;white-space:nowrap}
  .url b{font-weight:700}
  .swoosh{position:absolute;left:0;bottom:0}
</style>
</head>
<body>

<!-- Card 1: full blue with web address -->
<section class="card card--blue col-a row-1">
  <div class="glow"></div>
  <p class="url">www.<b>brighthorizonpassage</b>.example</p>
</section>

<!-- Card 2: contact block left, wordmark right, email band -->
<section class="card col-b row-1">
  <div class="brand" style="right:14px;top:26px"><span class="brand__line">Bright</span><span class="brand__line">Horizon Passage</span><span class="brand__mark"></span></div>
  <p class="text" style="left:13px;top:36px"><span class="strong-blue">Lorna Pickett</span></p>
  <p class="text" style="left:13px;top:58px">5427 Amber Hollow Lane<br>Ashford Bay, NC 28999<br>(770) 481-3027<br>Fax (555) 317-9042</p>
  <div class="band" style="bottom:0;height:50px"></div>
  <p class="text email" style="right:14px;bottom:17px;color:#fff;font-size:12px">lorna@<b>brighthorizonpassage</b>.example</p>
</section>

<!-- Card 3: centred layout on white -->
<section class="card col-a row-2">
  <div class="brand" style="left:96px;top:34px"><span class="brand__line">Bright</span><span class="brand__line">Horizon Passage</span><span class="brand__mark"></span></div>
  <p class="script center" style="top:90px;color:var(--ink)">Lorna Pickett</p>
  <div class="rule" style="left:127px;width:94px;top:122px"></div>
  <p class="text center" style="top:133px">5427 Amber Hollow Lane, Ashford Bay, NC 28999<br>(770) 481-3027 &nbsp;Fax (555) 317-9042<br><span class="strong-blue">lorna@brighthorizonpassage.example</span></p>
</section>

<!-- Card 4: right aligned on white -->
<section class="card col-b row-2">
  <div class="brand" style="right:14px;top:26px"><span class="brand__line">Bright</span><span class="brand__line">Horizon Passage</span><span class="brand__mark"></span></div>
  <p class="text right" style="right:16px;top:86px"><i class="name-bold">Lorna Pickett</i><br>5427 Amber Hollow Lane<br>Ashford Bay, NC 28999<br>(770) 481-3027<br>Fax (555) 317-9042</p>
  <p class="text right email" style="right:16px;bottom:12px;color:var(--blue);font-size:12.5px">lorna@<b>brighthorizonpassage</b>.example</p>
</section>

<!-- Card 5: white top, blue lower panel -->
<section class="card col-a row-3">
  <div class="brand" style="left:96px;top:30px"><span class="brand__line">Bright</span><span class="brand__line">Horizon Passage</span><span class="brand__mark"></span></div>
  <div class="band" style="top:100px;bottom:0"></div>
  <p class="script center" style="top:104px;color:#fff">Lorna Pickett</p>
  <div class="rule rule--white" style="left:118px;width:112px;top:136px"></div>
  <p class="text center" style="top:148px;color:#fff">5427 Amber Hollow Lane, Ashford Bay, NC 28999<br>(770) 481-3027 &nbsp;Fax (555) 317-9042<br>lorna@<b>brighthorizonpassage</b>.example</p>
</section>

<!-- Card 6: right aligned with curved email band -->
<section class="card col-b row-3">
  <div class="brand" style="right:14px;top:26px"><span class="brand__line">Bright</span><span class="brand__line">Horizon Passage</span><span class="brand__mark"></span></div>
  <p class="script right" style="right:16px;top:86px">Lorna Pickett</p>
  <div class="rule" style="right:16px;width:120px;top:118px"></div>
  <p class="text right" style="right:16px;top:128px">5427 Amber Hollow Lane, Ashford Bay, NC 28999</p>
  <p class="text right" style="right:16px;top:146px"><span class="lbl">t</span>(770) 481-3027<span class="lbl lbl-gap">f</span>(555) 317-9042</p>
  <svg class="swoosh" width="349" height="44" viewBox="0 0 349 44" aria-hidden="true">
    <path d="M40 44 C48 14 70 6 110 6 L349 6 L349 44 Z" fill="var(--blue)"/>
  </svg>
  <p class="text right" style="right:16px;bottom:10px;color:#fff;font-size:12px">lorna@brighthorizonpassage.example</p>
</section>

<!-- Card 7: left aligned with curved email tab -->
<section class="card col-a row-4">
  <div class="brand" style="left:18px;top:34px"><span class="brand__line">Bright</span><span class="brand__line">Horizon Passage</span><span class="brand__mark"></span></div>
  <p class="script" style="left:18px;top:96px;color:var(--blue)">Lorna Pickett</p>
  <p class="text" style="left:18px;top:134px">5427 Amber Hollow Lane, Ashford Bay, NC 28999</p>
  <p class="text" style="left:18px;top:154px"><span class="lbl">t</span>(770) 481-3027<span class="lbl lbl-gap">f</span>(555) 317-9042</p>
  <svg class="swoosh" width="349" height="40" viewBox="0 0 349 40" aria-hidden="true">
    <path d="M0 0 L260 0 C285 0 296 14 300 40 L0 40 Z" fill="var(--blue)"/>
  </svg>
  <p class="text" style="left:18px;bottom:11px;color:var(--blue-light);font-size:12px">lorna@brighthorizonpassage.example</p>
</section>

<!-- Card 8: full blue centred -->
<section class="card card--blue col-b row-4">
  <div class="brand brand--white" style="left:96px;top:34px"><span class="brand__line">Bright</span><span class="brand__line">Horizon Passage</span><span class="brand__mark"></span></div>
  <p class="script center" style="top:94px;color:#fff">Lorna Pickett</p>
  <div class="rule rule--white" style="left:118px;width:112px;top:126px"></div>
  <p class="text center" style="top:138px;color:#fff">5427 Amber Hollow Lane, Ashford Bay, NC 28999<br>(770) 481-3027 &nbsp;Fax (555) 317-9042<br>lorna@<b>brighthorizonpassage</b>.example</p>
</section>

</body>
</html>
```